Velvo Leaf needs a luxury packaging design

I'm starting a tea brand from the ground up. The working name as of now is Velvo Leaf. I intend for it to be a luxury loose leaf tea brand.

I want the aesthetic of it to be luxurious in nature. The color schemes that I am liking right now include black, gold, silver, rose gold and anything along that luxury feel line. One of the things I love most is UNIQUE packaging of the tea itself. I'll attach inspiration below.

I want the consumer every single time they use this product to feel like it is an experience. The person I choose will also be the person I consider for all further needs on a design basis moving forward if they would like to continue to work with me.

This is a really great opportunity to work with a luxury line that also does social good as some proceeds from each purchase will go to a mental health awareness cause.

The key is for the packaging to represent luxury, give off a unique feel that gets the consumer excited to see it and show it off to their peers on social media

Target Market(s)

The Modern Millenial, 21-40 (bullseye 28). He or she is a young professional that has a disposable income in which they do like to indulge with. They balance their demanding work schedules well and they have a work hard/play hard mindset. This professional is more likely to order their daily coffee from Brewhaven as opposed to Gus Pellery and their social media profiles are a big indicator as to their hobbies and lifestyles outside of their work environment. They enjoy shopping at stores like Ondi, Valkorn, Fenwire/FenMan and for special occasions are willing to splurge at stores like Marlow's, Maison Verdal and… They live a pretty active lifestyle and are highly influenced by social media trending products

Requirements
Must have
• Luxurious, must have exclusive look
Nice to have
• unique packaging
• viral inspired design
Should not have
• brown color, childish feel, bubble letters

```html
<!DOCTYPE html>
<html lang="en">
<head>
<meta charset="utf-8">
<title>Velvo Leaf — Green Tea Label</title>
<link rel="stylesheet" href="https://fonts.googleapis.com/css2?family=Play:wght@400;700&display=swap">
<style>
  :root {
    --backdrop: #d9d9d9;
    --label-black: #0b0b0b;
    --label-black-soft: #1a1a1a;
    --gold-dark: #b8650c;
    --gold: #f3a22a;
    --gold-light: #ffc35a;
    --leaf-green: #8cc63f;
    --rule-green: #6fa83a;
    --text-light: #e8e8e8;
  }
  * { box-sizing: border-box; margin: 0; padding: 0; }
  html, body {
    width: 1200px; height: 1200px; overflow: hidden;
    background: var(--backdrop);
    font-family: "Play", sans-serif;
  }
  .canvas { position: relative; width: 1200px; height: 1200px; }

  /* Round lid label */
  .lid-label {
    position: absolute; left: 60px; top: 385px;
    width: 420px; height: 420px; border-radius: 50%;
    background: var(--label-black);
    display: flex; align-items: center; justify-content: center;
  }
  .lid-label__ring {
    position: absolute; inset: 26px; border-radius: 50%;
    border: 4px solid var(--gold);
    box-shadow: 0 0 0 1px var(--gold-dark);
  }
  .brand-name {
    color: var(--text-light); font-weight: 400;
    letter-spacing: 1px; white-space: nowrap;
  }
  .lid-label .brand-name { font-size: 34px; }

  /* Wrap label */
  .wrap-label {
    position: absolute; left: 540px; top: 313px;
    width: 620px; height: 573px;
    background: radial-gradient(ellipse at 50% 45%, var(--label-black-soft), var(--label-black) 75%);
  }
  .gold-band { position: absolute; left: 0; right: 0; height: 20px; }
  .gold-band::before, .gold-band::after {
    content: ""; position: absolute; left: 0; right: 0;
    background: linear-gradient(90deg, var(--gold-dark), var(--gold) 30%, var(--gold-light) 55%, var(--gold) 80%, var(--gold-dark));
  }
  .gold-band::before { top: 0; height: 4px; }
  .gold-band::after { top: 9px; height: 9px; }
  .gold-band--top { top: 26px; }
  .gold-band--bottom { top: 535px; }

  .wrap-label .brand-name {
    position: absolute; top: 96px; left: 0; right: 0;
    text-align: center; font-size: 30px;
  }
  .product-title {
    position: absolute; top: 238px; left: 0; right: 0;
    text-align: center; font-size: 62px; font-weight: 700;
    color: var(--leaf-green); letter-spacing: 1px;
  }
  .product-info { position: absolute; left: 150px; width: 330px; top: 330px; }
  .product-info__desc {
    color: var(--text-light); font-size: 14.5px; line-height: 20px;
    padding-bottom: 6px; border-bottom: 1.5px dashed var(--rule-green);
  }
  .spec-row {
    display: flex; height: 34px; align-items: center;
    border-bottom: 1.5px dashed var(--rule-green);
    color: var(--text-light); font-size: 15px;
  }
  .spec-row__key { padding-left: 6px; }
  .spec-row__value {
    height: 24px; display: flex; align-items: center;
    border-left: 1.5px dashed var(--rule-green); padding-left: 26px;
  }
  .spec-row--class .spec-row__key { width: 120px; }
  .spec-row--origin .spec-row__key { width: 185px; }
  .spec-row--origin .spec-row__value { padding-left: 50px; }
  .spec-row--weight .spec-row__key { width: 155px; }
  .spec-row--weight .spec-row__value { padding-left: 40px; }
</style>
</head>
<body>
<main class="canvas">
  <section class="lid-label" aria-label="Round lid label">
    <div class="lid-label__ring"></div>
    <span class="brand-name">Velvo Leaf</span>
  </section>

  <section class="wrap-label" aria-label="Tin wrap label">
    <div class="gold-band gold-band--top"></div>
    <span class="brand-name">Velvo Leaf</span>
    <h1 class="product-title">Green Tea</h1>
    <div class="product-info">
      <p class="product-info__desc">Made with steamed tea leaves. Aids in weight loss, cancer prevention and stoke prevention.</p>
      <div class="spec-row spec-row--class"><span class="spec-row__key">Class:</span><span class="spec-row__value">Green tea</span></div>
      <div class="spec-row spec-row--origin"><span class="spec-row__key">Origin:</span><span class="spec-row__value">India</span></div>
      <div class="spec-row spec-row--weight"><span class="spec-row__key">Net Weight:</span><span class="spec-row__value">40 gm.</span></div>
    </div>
    <div class="gold-band gold-band--bottom"></div>
  </section>
</main>
</body>
</html>
```